Dynamic Business Card for Sports Supplements Company

Hi! I'm looking for an awesome business card to match my existing sports supplement company. I have uploaded my current company logo and screenshot of the front page of my website.

I would like to have something dynamic and interesting and utilize the colors in the website - the reds and purples

The business card should be double sided and focus on a unique eye-catching design on the back and include all the relevant company info.

Most importantly, it should say somewhere: "Sign up on our website for a coupon code."

Target Market(s)

Mostly for women gym goers but it shouldn't be too feminine. It should be in keeping with the website design. It should flow and clearly be connected to it

Industry/Entity Type

Business

Contact Information for Business Card

Colleen M. Varga
CEO
CVarga@Vitalorexco.example
www.vitalorexco.example
555.014.3827
P.O. Box 48317
Lindenvale, Westmont 00000

Sign up on our website for a coupon code

Font styles to use
Serif
Sans Serif
Other font styles liked:
• Novecento font family and "Vitalorex" is in AR Destine font

Requirements
Must have
• One side should be a bold Vitalorex logo design. Even just the symbol itself may be o.k. (see attached file)

```html
<!DOCTYPE html>
<html lang="en">
<head>
<meta charset="utf-8">
<title>Vitalorex Business Card</title>
<link rel="stylesheet" href="https://fonts.googleapis.com/css2?family=Open+Sans:wght@400;600;700;800&display=swap">
<style>
  :root {
    --bg: #2b2b2d;
    --purple: #4a1d63;
    --purple-deep: #3f1757;
    --red: #e5252a;
    --ink: #1e1e1e;
    --white: #ffffff;
  }
  * { box-sizing: border-box; margin: 0; padding: 0; }
  html, body { width: 1200px; height: 880px; overflow: hidden; }
  body {
    background: var(--bg);
    font-family: "Open Sans", Arial, sans-serif;
    position: relative;
  }
  .card {
    position: absolute;
    left: 270px;
    width: 660px;
    height: 377px;
    border-radius: 18px;
    overflow: hidden;
    box-shadow: 0 14px 30px rgba(0,0,0,.45);
  }
  .card--front {
    top: 40px;
    background: linear-gradient(135deg, var(--purple) 0%, var(--purple-deep) 100%);
    color: var(--white);
    text-align: center;
  }
  .brand {
    display: inline-flex;
    flex-direction: column;
    align-items: center;
  }
  .card--front .brand { margin-top: 120px; }
  .brand__name {
    font-weight: 800;
    font-size: 54px;
    letter-spacing: 2px;
    line-height: 1;
    text-transform: uppercase;
  }
  .brand__tagline {
    font-weight: 600;
    font-size: 11px;
    letter-spacing: 3.2px;
    text-transform: uppercase;
    margin-top: 6px;
  }
  .promo {
    margin-top: 40px;
    font-size: 19px;
    font-weight: 400;
  }
  .promo__action { color: var(--red); }

  .card--back {
    top: 463px;
    background: var(--white);
    color: var(--ink);
  }
  .card--back .brand {
    position: absolute;
    left: 60px;
    top: 90px;
    color: var(--ink);
  }
  .card--back .brand__name { font-size: 46px; }
  .card--back .brand__tagline { font-size: 9.5px; letter-spacing: 2.6px; }
  .social {
    position: absolute;
    right: 40px;
    top: 30px;
    display: flex;
    gap: 10px;
  }
  .social__dot {
    width: 26px; height: 26px;
    border: 2px solid var(--ink);
    border-radius: 50%;
  }
  .divider {
    position: absolute;
    left: 120px;
    right: 50px;
    top: 212px;
    height: 1.5px;
    background: var(--red);
  }
  .person {
    position: absolute;
    right: 50px;
    top: 176px;
    text-align: right;
  }
  .person__name { font-weight: 700; font-size: 24px; line-height: 1.2; }
  .person__role {
    color: var(--red);
    font-size: 16px;
    margin-top: 8px;
    letter-spacing: 1px;
  }
  .contact {
    position: absolute;
    left: 60px;
    top: 260px;
    list-style: none;
    font-size: 17px;
    line-height: 1.45;
  }
  .contact__item { display: flex; align-items: center; gap: 10px; }
  .contact__icon {
    width: 20px; height: 20px;
    background: var(--red);
    border-radius: 4px;
    flex: none;
  }
  .address {
    position: absolute;
    right: 50px;
    top: 268px;
    text-align: right;
    font-style: normal;
    font-size: 17px;
    line-height: 1.45;
  }
</style>
</head>
<body>

<section class="card card--front" aria-label="Card front">
  <div class="brand">
    <span class="brand__name">Vitalorex</span>
    <span class="brand__tagline">Your performance partner</span>
  </div>
  <p class="promo"><span class="promo__action">Sign up</span> on our website for a coupon code</p>
</section>

<section class="card card--back" aria-label="Card back">
  <div class="social" aria-hidden="true">
    <span class="social__dot"></span>
    <span class="social__dot"></span>
    <span class="social__dot"></span>
    <span class="social__dot"></span>
  </div>

  <div class="brand">
    <span class="brand__name">Vitalorex</span>
    <span class="brand__tagline">Your performance partner</span>
  </div>

  <div class="person">
    <p class="person__name">Colleen M. Varga</p>
    <p class="person__role">CEO</p>
  </div>

  <div class="divider"></div>

  <ul class="contact">
    <li class="contact__item">
      <svg class="contact__icon" viewBox="0 0 20 20" aria-hidden="true">
        <path d="M6 4.5c.6 0 1 .4 1.2 1l.6 2c.1.4 0 .8-.3 1.1l-1 .8c.8 1.6 2.1 2.9 3.7 3.7l.8-1c.3-.3.7-.4 1.1-.3l2 .6c.6.2 1 .6 1 1.2v1.4c0 .6-.5 1-1.1 1C9.3 16 4 10.7 4 5.6c0-.6.4-1.1 1-1.1z" fill="#fff"/>
      </svg>
      <span>555.014.3827</span>
    </li>
    <li class="contact__item">
      <svg class="contact__icon" viewBox="0 0 20 20" aria-hidden="true">
        <rect x="4" y="6" width="12" height="8.5" fill="none" stroke="#fff" stroke-width="1.4"/>
        <path d="M4 6l6 5 6-5" fill="none" stroke="#fff" stroke-width="1.4"/>
      </svg>
      <span>CVarga@Vitalorexco.example</span>
    </li>
    <li class="contact__item">
      <svg class="contact__icon" viewBox="0 0 20 20" aria-hidden="true">
        <circle cx="10" cy="10" r="5.5" fill="none" stroke="#fff" stroke-width="1.3"/>
        <ellipse cx="10" cy="10" rx="2.3" ry="5.5" fill="none" stroke="#fff" stroke-width="1.1"/>
        <path d="M4.5 10h11" stroke="#fff" stroke-width="1.1"/>
      </svg>
      <span>www.vitalorexco.example</span>
    </li>
  </ul>

  <address class="address">
    P.O. Box 48317<br>
    Lindenvale, Westmont 00000
  </address>
</section>

</body>
</html>
```